Larchmont Holdings Needs New Stationery Design

We need new clean and white stationery for our property management company based in Winnipeg, Manitoba, Canada. We manage condominium and commercial properties. Additionally, we do real estate development and commercial leasing.

We'll require the following:
- Business cards
- Letterhead*
- Envelope (we mainly use #10, single window envelope)
- Fax Cover Sheet
- *Electronic version of the letterhead that works in Google Docs (.jpg for top header)

Industry/Entity Type

Property Management

```html
<!DOCTYPE html>
<html lang="en">
<head>
<meta charset="utf-8">
<title>Larchmont Holdings — Business Card</title>
<link rel="stylesheet" href="https://fonts.googleapis.com/css2?family=Source+Sans+3:wght@400;600;700;800&display=swap">
<style>
  :root {
    --navy: #263f73;
    --cyan: #1aa3c8;
    --grey-text: #5f6166;
    --ink: #1b1b1b;
    --paper: #ffffff;
    --backdrop: #ececec;
    --edge: #8a8a8a;
  }
  * { box-sizing: border-box; margin: 0; padding: 0; }
  html, body { width: 1200px; height: 1052px; overflow: hidden; }
  body {
    position: relative;
    background: var(--backdrop);
    font-family: "Source Sans 3", "Helvetica Neue", Arial, sans-serif;
  }
  .card {
    position: absolute;
    width: 762px;
    height: 436px;
    background: var(--paper);
    border: 1px solid var(--edge);
    overflow: hidden;
  }
  .card--front { left: 71px; top: 64px; }
  .card--back  { left: 371px; top: 556px; }

  /* Company name set in text */
  .wordmark {
    position: absolute;
    color: var(--navy);
    font-weight: 800;
    font-size: 72px;
    line-height: 0.92;
    letter-spacing: -1px;
  }
  .wordmark__line { display: block; }
  .card--front .wordmark { left: 52px; top: 78px; }
  .card--back .wordmark { left: 0; right: 0; top: 108px; text-align: center; }

  .address {
    position: absolute;
    right: 22px; top: 104px;
    text-align: right;
    font-style: normal;
    color: var(--grey-text);
    font-size: 19px;
    line-height: 24px;
  }
  .holder {
    position: absolute;
    left: 72px; top: 264px;
    color: var(--cyan);
    white-space: nowrap;
  }
  .holder__name { font-size: 23px; font-weight: 700; }
  .holder__role { font-size: 17px; font-weight: 400; }

  .wave { position: absolute; left: 0; top: 0; width: 762px; height: 436px; }

  .contacts {
    position: absolute;
    right: 20px; top: 308px;
    list-style: none;
    color: var(--paper);
    font-size: 18px;
    line-height: 27px;
    text-align: right;
  }
  .contacts li { display: flex; justify-content: flex-end; align-items: center; gap: 12px; }
  .contacts svg { width: 15px; height: 15px; flex: none; }

  .web {
    position: absolute;
    left: 0; right: 0; top: 352px;
    text-align: center;
    color: var(--ink);
    font-size: 17px;
    letter-spacing: 2px;
  }
</style>
</head>
<body>

<section class="card card--front" aria-label="Business card front">
  <svg class="wave" viewBox="0 0 762 436" aria-hidden="true">
    <path class="wave__ribbon" fill="var(--cyan)"
      d="M0,338 C150,400 330,420 470,345 S660,215 762,185 L762,200 C670,222 560,292 490,345 C350,451 140,425 0,372 Z"/>
    <path class="wave__base" fill="var(--navy)"
      d="M0,410 C230,445 420,415 540,345 S705,232 762,220 L762,436 L0,436 Z"/>
    <path class="wave__gap" fill="none" stroke="var(--paper)" stroke-width="7"
      d="M0,410 C230,445 420,415 540,345 S705,232 762,220"/>
  </svg>

  <div class="wordmark">
    <span class="wordmark__line">Larchmont</span>
    <span class="wordmark__line">Holdings</span>
  </div>

  <address class="address">
    Larchmont Holdings Corp.<br>
    214 Elm Crescent<br>
    Winnipeg, MB R3M 1K7
  </address>

  <p class="holder"><span class="holder__name">Adrian Kessler ,</span> <span class="holder__role">President &amp; CEO</span></p>

  <ul class="contacts">
    <li>(204)555-0142
      <svg viewBox="0 0 16 16" aria-label="Phone"><circle cx="8" cy="8" r="7" fill="none" stroke="currentColor" stroke-width="1.4"/><path fill="currentColor" d="M5.2 4.2l1.5-.3.8 2-1 .7c.5 1.1 1.2 1.8 2.2 2.3l.7-1 2 .8-.3 1.5c-3.2.1-6-2.8-5.9-6z"/></svg>
    </li>
    <li>(204)555-0143
      <svg viewBox="0 0 16 16" aria-label="Fax"><rect x="4" y="2" width="8" height="4" fill="currentColor"/><rect x="1.5" y="6.5" width="13" height="6" rx="1" fill="currentColor"/><rect x="4" y="10" width="8" height="4" fill="currentColor" stroke="var(--navy)" stroke-width="1"/></svg>
    </li>
    <li>info@larchmontholdings.ca
      <svg viewBox="0 0 16 16" aria-label="Email"><rect x="1.5" y="3.5" width="13" height="9" fill="currentColor"/><path d="M1.5 3.8l6.5 5 6.5-5" fill="none" stroke="var(--navy)" stroke-width="1.2"/></svg>
    </li>
    <li>www.larchmontholdings.ca
      <svg viewBox="0 0 16 16" aria-label="Website"><g fill="none" stroke="currentColor" stroke-width="1.2"><circle cx="8" cy="8" r="6.5"/><ellipse cx="8" cy="8" rx="3" ry="6.5"/><path d="M1.5 8h13M2.8 4.5h10.4M2.8 11.5h10.4"/></g></svg>
    </li>
  </ul>
</section>

<section class="card card--back" aria-label="Business card back">
  <div class="wordmark">
    <span class="wordmark__line">Larchmont</span>
    <span class="wordmark__line">Holdings</span>
  </div>
  <p class="web">www.larchmontholdings.ca</p>
</section>

</body>
</html>
```